Sports Therapy and Personal Training

I need a business card design for a new business based in Toronto called "Holbrin Athletics" I am a sports therapist as well as a strength and conditioning coach, therefore I work mainly with high level athletes and physically active people. I am starting my own therapy/training business. The services I will be offering include fitness consultation, personal training, athlete assessments, and rehabilitation therapy. These services will be delivered in peoples homes and/or a facility in which I rent space.

The final design should communicate "high-end" and "quality"

Target Market(s)

athletes and physically active people

Industry/Entity Type

Fitness

Requirements
Must have
• 1. The business logo - files attached

2. my name and credentials

Derek Falloway - CAT(C), CK, CSCS,

Certified Athletic Therapist
Strength and Conditioning Specialist

3. website - www.holbrinathletics.example

4. email address - derek@holbrinathletics.example

5. phone number

```html
<!DOCTYPE html>
<html lang="en">
<head>
<meta charset="utf-8">
<title>Holbrin Athletics — Business Cards</title>
<link href="https://fonts.googleapis.com/css2?family=Montserrat:wght@600;700&family=Questrial&display=swap" rel="stylesheet">
<style>
  :root {
    --stage: #323232;
    --card-light: #ffffff;
    --card-edge: #e4e4e6;
    --card-dark: #6e6f73;
    --card-dark-edge: #55565a;
    --tab-gray: #6c6d71;
    --tab-white: #ffffff;
    --ink: #3b3c40;
    --ink-soft: #8a8b8f;
    --accent: #c8161d;
    --rule: #e9b7b9;
  }
  * { box-sizing: border-box; margin: 0; padding: 0; }
  html, body { width: 1200px; height: 702px; overflow: hidden; }
  body { background: var(--stage); position: relative; font-family: "Questrial", sans-serif; }

  .card {
    position: absolute;
    width: 585px; height: 334px;
    border-radius: 16px;
    background: radial-gradient(ellipse at 45% 45%, var(--card-light) 55%, var(--card-edge) 100%);
    overflow: hidden;
  }
  .card--small { transform: scale(0.718); transform-origin: top left; }
  .card--dark { background: radial-gradient(ellipse at 50% 40%, var(--card-dark) 40%, var(--card-dark-edge) 100%); }

  .card--front-small { left: 90px; top: 73px; }
  .card--back-small  { left: 673px; top: 75px; }
  .card--front       { left: 11px; top: 349px; }
  .card--back        { left: 605px; top: 349px; }

  .tab { position: absolute; top: 26px; bottom: 24px; width: 15px; background: var(--tab-gray); }
  .tab--left { left: 0; border-radius: 0 6px 6px 0; }
  .tab--right { right: 0; border-radius: 6px 0 0 6px; }
  .card--dark .tab { background: var(--tab-white); }

  .brand { position: absolute; text-align: center; transform: translateX(-50%); white-space: nowrap; }
  .brand__name {
    display: inline-flex; align-items: center; gap: 10px;
    font-family: "Montserrat", sans-serif; font-weight: 700;
    text-transform: uppercase; color: var(--ink); letter-spacing: 0.5px;
  }
  .brand__mark { width: 0.7em; height: 0.7em; background: var(--accent); }
  .brand__tagline {
    margin-top: 4px; font-size: 8.5px; letter-spacing: 0.6px;
    text-transform: uppercase; color: var(--ink-soft);
  }
  .card--dark .brand__name { color: #f2f2f2; }
  .card--dark .brand__tagline { color: #c9c9cc; }

  .brand--hero { left: 293px; top: 120px; }
  .brand--hero .brand__name { font-size: 30px; }
  .brand--hero .brand__tagline { font-size: 10.5px; }
  .brand--side { left: 152px; top: 150px; }
  .brand--side .brand__name { font-size: 19px; }
  .card--dark .brand--hero { left: 250px; top: 128px; }

  .person { position: absolute; right: 61px; top: 88px; text-align: right; }
  .person__name {
    font-family: "Montserrat", sans-serif; font-weight: 700;
    font-size: 23px; color: var(--accent); text-transform: uppercase; line-height: 1;
  }
  .person__creds { margin-top: 4px; font-size: 10.5px; color: var(--ink); }

  .roles { position: absolute; left: 316px; top: 146px; list-style: none; }
  .roles li {
    font-size: 9.5px; font-weight: 700; text-transform: uppercase;
    color: var(--ink); line-height: 13px; letter-spacing: 0.3px;
  }
  .roles li::before { content: "•"; margin-right: 6px; }

  .divider {
    position: absolute; left: 316px; top: 186px; width: 210px; height: 1px;
    background: linear-gradient(90deg, transparent, var(--rule) 40%, var(--rule) 60%, transparent);
  }

  .contact { position: absolute; left: 316px; top: 203px; list-style: none; }
  .contact li {
    display: flex; align-items: center; gap: 6px;
    font-size: 10px; text-transform: uppercase; color: var(--ink);
    height: 15px; letter-spacing: 0.3px;
  }
  .contact svg { width: 10px; height: 10px; fill: var(--ink); }
</style>
</head>
<body>

  <!-- Front, small -->
  <section class="card card--small card--dark card--front-small">
    <span class="tab tab--left"></span><span class="tab tab--right"></span>
    <div class="brand brand--hero">
      <div class="brand__name"><span class="brand__mark"></span>Holbrin Athletics</div>
      <div class="brand__tagline">Sports Medicine • Strength and Conditioning</div>
    </div>
  </section>

  <!-- Back, small -->
  <section class="card card--small card--back-small">
    <span class="tab tab--left"></span><span class="tab tab--right"></span>
    <div class="brand brand--side">
      <div class="brand__name"><span class="brand__mark"></span>Holbrin Athletics</div>
      <div class="brand__tagline">Sports Medicine • Strength and Conditioning</div>
    </div>
    <div class="person">
      <div class="person__name">Derek Falloway</div>
      <div class="person__creds">CAT(C), CK, CSCS</div>
    </div>
    <ul class="roles">
      <li>Certified Athletic Therapist</li>
      <li>Strength and Conditioning Specialist</li>
    </ul>
    <span class="divider"></span>
    <ul class="contact">
      <li><svg viewBox="0 0 10 10"><rect x="2.5" y="0" width="5" height="10" rx="1"/></svg>00 0000 0000</li>
      <li><svg viewBox="0 0 10 10"><path d="M0 2h10v6H0z M0 2l5 3.5L10 2" stroke="#fff" stroke-width="0.8"/></svg>derek@holbrinathletics.example</li>
      <li><svg viewBox="0 0 10 10"><circle cx="5" cy="5" r="4.5"/><path d="M0.5 5h9M5 0.5v9" stroke="#fff" stroke-width="0.8"/></svg>www.holbrinathletics.example</li>
    </ul>
  </section>

  <!-- Front, large -->
  <section class="card card--front">
    <span class="tab tab--left"></span><span class="tab tab--right"></span>
    <div class="brand brand--hero">
      <div class="brand__name"><span class="brand__mark"></span>Holbrin Athletics</div>
      <div class="brand__tagline">Sports Medicine • Strength and Conditioning</div>
    </div>
  </section>

  <!-- Back, large -->
  <section class="card card--back">
    <span class="tab tab--left"></span><span class="tab tab--right"></span>
    <div class="brand brand--side">
      <div class="brand__name"><span class="brand__mark"></span>Holbrin Athletics</div>
      <div class="brand__tagline">Sports Medicine • Strength and Conditioning</div>
    </div>
    <div class="person">
      <div class="person__name">Derek Falloway</div>
      <div class="person__creds">CAT(C), CK, CSCS</div>
    </div>
    <ul class="roles">
      <li>Certified Athletic Therapist</li>
      <li>Strength and Conditioning Specialist</li>
    </ul>
    <span class="divider"></span>
    <ul class="contact">
      <li><svg viewBox="0 0 10 10"><rect x="2.5" y="0" width="5" height="10" rx="1"/></svg>00 0000 0000</li>
      <li><svg viewBox="0 0 10 10"><path d="M0 2h10v6H0z M0 2l5 3.5L10 2" stroke="#fff" stroke-width="0.8"/></svg>derek@holbrinathletics.example</li>
      <li><svg viewBox="0 0 10 10"><circle cx="5" cy="5" r="4.5"/><path d="M0.5 5h9M5 0.5v9" stroke="#fff" stroke-width="0.8"/></svg>www.holbrinathletics.example</li>
    </ul>
  </section>

</body>
</html>
```